Elegant Financial Planning Business Card

Clearpath Wealth Advisory Pty Ltd requires an elegant business card that communicates simplicity, elegance and trust.
Attached card example of 'Varnoth' is very close to what I am looking for. Looking for black and white card.
Update 24/1/16: The attached Varnoth card is almost exactly what I am looking for. Although it is possible that alternative layouts may interest me, it is considerably more likely that I will proceed with a virtual clone of the "Varnoth' example.
Industry/Entity Type
Financial Planning
Contact Information for Business Card
In black font...
Front Details are (layout as per Dana Varnoth card picture):
Line1 - Name: Oliver Marsh
Line 2 - Company: Clearpath Wealth Advisory Pty Ltd
Line 3 - Address: Harbourview Plaza 3, Level 17, 58 Lomond Avenue, Bondi Junction NSW
Line 4
- Phone: 136 712
- Email: advice@cpwa-example.com.au
- Site: www.cpwa-example.com.au
Back details
1/ logo in position and dimensions as per attached layout
2. Bottom left (in smaller writing).
- Authorised Representative No. 517946
- Clearpath Wealth Advisory is a corporate authorised representative of Tarquay7 Capital Services Pty Ltd
- ABN 47 318 602 154
- AFSL No. 608139

```html
<!DOCTYPE html>
<html lang="en">
<head>
<meta charset="utf-8">
<title>Clearpath Wealth Advisory – Business Card</title>
<link rel="stylesheet" href="https://fonts.googleapis.com/css2?family=Tinos:wght@400;700&display=swap">
<style>
  :root {
    --backdrop: #3a322d;
    --card: #0d0d0d;
    --card-panel: #131313;
    --ink-light: #e6e6e6;
    --ink-soft: #c9c9c9;
    --mark: #d8d8d8;
  }
  * { box-sizing: border-box; margin: 0; padding: 0; }
  html, body { width: 1200px; height: 900px; overflow: hidden; }
  body {
    background: var(--backdrop);
    font-family: "Tinos", "Times New Roman", serif;
    color: var(--ink-light);
    position: relative;
  }
  .card {
    position: absolute;
    top: 290px;
    width: 540px;
    height: 320px;
    background: var(--card);
    box-shadow: 0 14px 30px rgba(0,0,0,0.45);
  }
  .card--front { left: 45px; }
  .card--back { left: 615px; }

  /* Front */
  .front-brand {
    position: absolute;
    left: 0; top: 0;
    width: 210px; height: 100%;
    display: flex; flex-direction: column;
    justify-content: center; align-items: center;
    gap: 12px;
  }
  .brand-square {
    width: 18px; height: 18px;
    background: var(--mark);
  }
  .brand-name {
    font-size: 19px;
    line-height: 1.2;
    text-align: center;
    color: var(--mark);
    font-weight: 400;
    padding: 0 18px;
  }
  .front-details {
    position: absolute;
    left: 210px; top: 0;
    width: 330px; height: 100%;
    background: var(--card-panel);
    padding: 70px 26px 0 26px;
  }
  .person-name {
    font-size: 22px;
    font-weight: 700;
    margin-bottom: 18px;
  }
  .address {
    font-size: 13.5px;
    line-height: 1.45;
    color: var(--ink-soft);
    margin-bottom: 14px;
  }
  .contact-list { list-style: none; }
  .contact-list li {
    display: flex; align-items: center; gap: 8px;
    font-size: 13.5px;
    line-height: 1.5;
    color: var(--ink-soft);
  }
  .contact-list svg { width: 11px; height: 11px; flex: none; fill: var(--ink-light); }

  /* Back */
  .back-brand {
    position: absolute;
    right: 34px; top: 38px;
    display: flex; align-items: center; gap: 10px;
  }
  .back-brand .brand-name { font-size: 17px; text-align: right; padding: 0; }
  .legal {
    position: absolute;
    left: 34px; bottom: 42px;
    width: 440px;
    font-size: 12.5px;
    line-height: 1.4;
    color: var(--ink-soft);
  }
  .legal p + p { margin-top: 10px; }
</style>
</head>
<body>
  <section class="card card--front" aria-label="Business card front">
    <div class="front-brand">
      <span class="brand-square" aria-hidden="true"></span>
      <p class="brand-name">Clearpath Wealth Advisory Pty Ltd</p>
    </div>
    <div class="front-details">
      <h1 class="person-name">Oliver Marsh</h1>
      <p class="address">Harbourview Plaza 3, Level 17, 58 Lomond Avenue, Bondi Junction NSW</p>
      <ul class="contact-list">
        <li><svg viewBox="0 0 16 16" aria-hidden="true"><path d="M3.6 1.2l2.3 2.6-1.3 1.9c.9 2 2.6 3.8 4.7 4.8l1.9-1.3 2.6 2.3-1.4 2.3C7.5 13.5 2.5 8.5 1.3 2.6z"/></svg>136 712</li>
        <li><svg viewBox="0 0 16 16" aria-hidden="true"><path d="M1 3h14v10H1z M2 4l6 5 6-5" fill="none" stroke="#e6e6e6" stroke-width="1.6"/></svg>advice@cpwa-example.com.au</li>
        <li><svg viewBox="0 0 16 16" aria-hidden="true"><circle cx="8" cy="8" r="6.5" fill="none" stroke="#e6e6e6" stroke-width="1.5"/><path d="M1.5 8h13M8 1.5c-3 3.5-3 9.5 0 13M8 1.5c3 3.5 3 9.5 0 13" fill="none" stroke="#e6e6e6" stroke-width="1.2"/></svg>www.cpwa-example.com.au</li>
      </ul>
    </div>
  </section>

  <section class="card card--back" aria-label="Business card back">
    <div class="back-brand">
      <p class="brand-name">Clearpath Wealth Advisory<br>Pty Ltd</p>
      <span class="brand-square" aria-hidden="true"></span>
    </div>
    <div class="legal">
      <p>Authorised Representative No. 517946</p>
      <p>Clearpath Wealth Advisory is a corporate authorised representative of Tarquay7 Capital Services Pty Ltd</p>
      <p>ABN 47 318 602 154<br>AFSL No. 608139</p>
    </div>
  </section>
</body>
</html>
```